Mobile app for checking bus arrival

I would like to make the UI much more beautiful and modern. The app is an app to check bus arrival in Singapore.
See here: https://apps.veltrixa.com/store/apps/details?id=com.ridetrk&hl=en

Based on the question from designers:

1. The first screen shows the favorite bus stop. Each item shows location / street, the top one is the location, second line is the street name. And the number is the bus stop code.

2. Please download the app and try bus stop code with 07589 or 10079, for example. It will bring you to the next screen.

3. The pencil allow you to select color theme, for the list item, and the header.

4. On the second screen, it will show up the list of bus route that available on that bus stop.

5. When you tap on one of them it will show you the 2 subsequent arrival time.

6. Each of the arrival time has the information of availability seats available, seats not available, no more space. (we can use green, yellow, red, respectively).

7. Each of the arrival time has the WAB indicator (Wheelchair availability). Show as icon is preferred.

7. KLV and DPWQ are the bus provider in Singapore. 48 means the route /service no.

Requirements:
And check the attachment, see screen 3. I need to add information about the space availability, which has 3 state: seats available, seats not available, no more space. (we can use green, yellow, red, respectively).

Please advise how to show the information.

Target Market(s)

Students, age below 35

Industry/Entity Type

Veltrixa

Requirements
Must have
• The app currently has the capabilities to select color theme, checkout screen1. It's the button and the list item color.
Nice to have
• Please download the app to see all available colors, and make suggestion to have better color pallete.

```html
<!DOCTYPE html>
<html lang="en">
<head>
<meta charset="utf-8">
<title>Bus Stop 07589 – Arrivals</title>
<link rel="stylesheet" href="https://fonts.googleapis.com/css2?family=Open+Sans:wght@300;400;600&display=swap">
<style>
  :root {
    --header-blue: #5680f2;
    --location-blue: #4f7ef5;
    --pin-blue: #6f96f8;
    --page-bg: #f3f3f3;
    --tile-grey: #e7e7e7;
    --route-red: #e24b4b;
    --route-purple: #a348e0;
    --white: #ffffff;
    --status-text: #111111;
    --dot-green: #4cc94c;
    --dot-grey: #d6d6d6;
    --dot-amber: #f5b800;
    --ad-dark: #2e2e2e;
  }
  * { box-sizing: border-box; margin: 0; padding: 0; }
  html, body { width: 676px; height: 1200px; overflow: hidden; }
  body {
    position: relative;
    background: var(--page-bg);
    font-family: "Open Sans", Arial, sans-serif;
    color: var(--white);
  }

  /* Status bar */
  .status-bar {
    position: absolute; left: 0; top: 0; width: 676px; height: 42px;
    background: var(--header-blue); color: var(--status-text);
    font-size: 22px; display: flex; align-items: center;
  }
  .status-bar .carrier { position: absolute; left: 8px; top: 6px; display: flex; align-items: center; gap: 6px; }
  .status-bar .time { position: absolute; left: 0; right: 0; top: 6px; text-align: center; font-weight: 600; }
  .status-bar .battery { position: absolute; right: 10px; top: 6px; display: flex; align-items: center; gap: 8px; }

  /* Header */
  .app-header {
    position: absolute; left: 0; top: 42px; width: 676px; height: 93px;
    background: var(--header-blue);
  }
  .app-header .back { position: absolute; left: 30px; top: 24px; }
  .app-header .stop-code {
    position: absolute; left: 0; right: 0; top: 20px; text-align: center;
    font-size: 34px; font-weight: 400; letter-spacing: 1px;
  }
  .app-header .actions { position: absolute; right: 22px; top: 24px; display: flex; gap: 26px; align-items: center; }

  /* Location bar */
  .location-bar {
    position: absolute; left: 0; top: 135px; width: 676px; height: 102px;
    background: var(--location-blue); text-align: center;
  }
  .location-bar .pin-box {
    position: absolute; left: 0; top: 0; width: 74px; height: 102px;
    background: var(--pin-blue); display: flex; align-items: center; justify-content: center;
  }
  .location-bar .place { position: absolute; left: 74px; right: 0; top: 10px; font-size: 34px; font-weight: 400; }
  .location-bar .street { position: absolute; left: 74px; right: 0; top: 55px; font-size: 20px; }

  /* Route tiles */
  .route-tile {
    position: absolute; width: 313px; height: 218px; border-radius: 3px;
  }
  .route-tile .number {
    position: absolute; left: 0; right: 0; top: 68px; text-align: center;
    font-size: 64px; font-weight: 400; line-height: 1;
  }
  .route-tile .operator { position: absolute; left: 22px; bottom: 18px; font-size: 28px; }
  .tile-red { background: var(--route-red); color: var(--white); }
  .tile-purple { background: var(--route-purple); color: var(--white); }
  .tile-grey { background: var(--tile-grey); }
  .tile-grey.text-red { color: var(--route-red); }
  .tile-grey.text-purple { color: var(--route-purple); }
  .col-left { left: 17px; }
  .col-right { left: 344px; }

  /* Expanded arrival tile */
  .arrival-tile { background: var(--white); color: var(--route-red); }
  .arrival-tile .tile-bar {
    position: absolute; left: 0; top: 0; width: 313px; height: 55px;
    background: var(--route-red); border-radius: 3px 3px 0 0; color: var(--white);
  }
  .arrival-tile .wab-label { position: absolute; left: 78px; top: 8px; font-size: 28px; }
  .arrival-tile .bus-icon { position: absolute; left: 20px; top: 7px; }
  .arrival-tile .service-box {
    position: absolute; right: 3px; top: 5px; width: 104px; height: 43px;
    background: var(--white); color: var(--route-red);
    font-size: 28px; text-align: center; line-height: 43px;
  }
  .arrival-slot {
    position: absolute; top: 82px; width: 90px; height: 88px;
    background: var(--route-red); color: var(--white);
    font-size: 27px; text-align: center; line-height: 88px;
  }
  .arrival-slot.first { left: 42px; }
  .arrival-slot.second { left: 179px; }
  .load-dots { position: absolute; top: 178px; display: flex; gap: 6px; }
  .load-dots.first { left: 60px; }
  .load-dots.second { left: 197px; }
  .dot { width: 13px; height: 13px; border-radius: 50%; background: var(--dot-grey); }
  .dot.green { background: var(--dot-green); }
  .dot.amber { background: var(--dot-amber); }

  /* Ad bar */
  .ad-bar {
    position: absolute; left: 0; top: 1108px; width: 676px; height: 92px;
    background: var(--ad-dark);
  }
  .ad-banner {
    position: absolute; left: 37px; top: 0; width: 601px; height: 92px; overflow: hidden;
    background: linear-gradient(90deg, #c98a1c 0%, #e3a83a 35%, #a9681a 65%, #d79b33 100%);
  }
  .ad-banner .ad-size { position: absolute; left: 24px; top: 4px; font-size: 33px; color: var(--white); line-height: 40px; white-space: nowrap; }
  .ad-banner .ad-brand {
    position: absolute; left: 300px; top: 22px; height: 48px; color: var(--white);
    display: flex; align-items: center; gap: 14px; white-space: nowrap;
  }
  .ad-banner .ad-brand .mark { width: 46px; height: 46px; background: var(--white); flex: none; }
  .ad-banner .ad-brand .name { font-size: 36px; line-height: 48px; }
  .ad-banner .ad-brand .by { font-size: 14px; line-height: 14px; align-self: flex-end; margin-bottom: 6px; margin-left: -6px; }
  .ad-info {
    position: absolute; left: 8px; top: 66px; width: 22px; height: 22px; border-radius: 50%;
    border: 2px solid #bbbbbb; color: #bbbbbb; font-size: 14px; text-align: center; line-height: 18px;
  }
</style>
</head>
<body>

<header class="status-bar">
  <div class="carrier">
    <svg width="62" height="14" viewBox="0 0 62 14"><g fill="#111"><circle cx="6" cy="7" r="5.5"/><circle cx="18" cy="7" r="5.5"/><circle cx="30" cy="7" r="5.5"/></g><g fill="none" stroke="#111" stroke-width="1.2"><circle cx="42" cy="7" r="5"/><circle cx="54" cy="7" r="5"/></g></svg>
    <span>CARRA</span>
    <svg width="24" height="18" viewBox="0 0 24 18"><path d="M12 17 L2 6 A14 14 0 0 1 22 6 Z" fill="#111"/></svg>
  </div>
  <div class="time">4:21 PM</div>
  <div class="battery">
    <svg width="14" height="22" viewBox="0 0 14 22"><path d="M2 6 L12 15 L7 20 L7 2 L12 7 L2 16" fill="none" stroke="#5a5a5a" stroke-width="1.5"/></svg>
    <span>22%</span>
    <svg width="46" height="22" viewBox="0 0 46 22"><rect x="1" y="1" width="40" height="20" rx="3" fill="none" stroke="#111" stroke-width="1.6"/><rect x="4" y="4" width="9" height="14" fill="#111"/><rect x="42" y="7" width="3" height="8" fill="#111"/></svg>
  </div>
</header>

<nav class="app-header">
  <svg class="back" width="26" height="46" viewBox="0 0 26 46"><path d="M23 2 L3 23 L23 44" fill="none" stroke="#fff" stroke-width="3"/></svg>
  <div class="stop-code">07589</div>
  <div class="actions">
    <svg width="46" height="44" viewBox="0 0 24 23"><path d="M12 1 L15 8.5 L23 9 L17 14 L19 22 L12 17.6 L5 22 L7 14 L1 9 L9 8.5 Z" fill="#fff"/></svg>
    <svg width="40" height="40" viewBox="0 0 40 40"><path d="M33 20 A13 13 0 1 1 20 7" fill="none" stroke="#fff" stroke-width="6"/><path d="M16 0 L28 7 L16 14 Z" fill="#fff"/></svg>
    <svg width="10" height="36" viewBox="0 0 10 36"><g fill="#fff"><circle cx="5" cy="5" r="4.5"/><circle cx="5" cy="18" r="4.5"/><circle cx="5" cy="31" r="4.5"/></g></svg>
  </div>
</nav>

<section class="location-bar">
  <div class="pin-box">
    <svg width="26" height="34" viewBox="0 0 26 34"><path d="M13 32 C5 21 2 16 2 12 A11 11 0 0 1 24 12 C24 16 21 21 13 32 Z" fill="none" stroke="#fff" stroke-width="2"/><circle cx="13" cy="12" r="4" fill="none" stroke="#fff" stroke-width="2"/></svg>
  </div>
  <div class="place">Opp Talvern ctr</div>
  <div class="street">ostel rd</div>
</section>

<main class="route-grid">
  <article class="route-tile arrival-tile col-left" style="top:251px">
    <div class="tile-bar">
      <svg class="bus-icon" width="40" height="40" viewBox="0 0 40 40"><g fill="none" stroke="#fff" stroke-width="2.4"><rect x="5" y="3" width="30" height="30" rx="6"/><rect x="9" y="8" width="22" height="12" rx="2"/><line x1="1" y1="12" x2="5" y2="12"/><line x1="35" y1="12" x2="39" y2="12"/><line x1="10" y1="33" x2="10" y2="38"/><line x1="30" y1="33" x2="30" y2="38"/><line x1="13" y1="12" x2="17" y2="10"/></g><circle cx="11" cy="26" r="2" fill="#fff"/><circle cx="29" cy="26" r="2" fill="#fff"/></svg>
      <span class="wab-label">WAB</span>
      <span class="service-box">120</span>
    </div>
    <div class="arrival-slot first">7</div>
    <div class="load-dots first"><span class="dot green"></span><span class="dot"></span><span class="dot"></span></div>
    <div class="arrival-slot second">21</div>
    <div class="load-dots second"><span class="dot"></span><span class="dot"></span><span class="dot amber"></span></div>
  </article>

  <article class="route-tile tile-red col-right" style="top:251px"><div class="number">57</div><div class="operator">klv</div></article>
  <article class="route-tile tile-red col-left" style="top:486px"><div class="number">131</div><div class="operator">klv</div></article>
  <article class="route-tile tile-grey text-red col-right" style="top:486px"><div class="number">851</div><div class="operator">dpwq</div></article>
  <article class="route-tile tile-grey text-purple col-left" style="top:721px"><div class="number">960</div><div class="operator">dpwq</div></article>
  <article class="route-tile tile-purple col-right" style="top:721px"><div class="number">2N</div><div class="operator">klv</div></article>
  <article class="route-tile tile-purple col-left" style="top:955px"><div class="number">2N</div></article>
  <article class="route-tile tile-grey col-right" style="top:955px"></article>
</main>

<aside class="ad-bar">
  <div class="ad-banner" role="img" aria-label="Test advertisement banner with warm golden background">
    <div class="ad-size">320x50<br>Test Banner</div>
    <div class="ad-brand"><span class="mark"></span><span class="name">AdNexa</span><span class="by">by Veltrixa</span></div>
  </div>
  <div class="ad-info">i</div>
</aside>

</body>
</html>
```